New Web Design Project

See attachments on the content and concept. Very important that the flow of the tiers stand out

Target Market(s)

Food and Beverage Manufacturing

Industry/Entity Type

Food and Beverage

Coding

Coded - Design and coding required

Number of Pages Required

3 page

Colors
0054AA
0677BA
7BADD7
CADEEF
E8F1F8

```html
<!DOCTYPE html>
<html lang="en">
<head>
<meta charset="utf-8">
<title>Northline Consulting Group — QFS Certification</title>
<link rel="stylesheet" href="https://fonts.googleapis.com/css2?family=Inter:wght@400;500;600;700&family=Playfair+Display:wght@600;700&display=swap">
<style>
:root{
  --blue-deep:#0054AA;
  --blue-mid:#0677BA;
  --blue-soft:#7BADD7;
  --blue-pale:#CADEEF;
  --blue-mist:#E8F1F8;
  --page:#F0F3F8;
  --band:#E3E9F3;
  --ink:#1B2230;
  --backdrop:#A0A3AB;
  --white:#FFFFFF;
  --serif:'Playfair Display', Georgia, serif;
  --sans:'Inter', Arial, sans-serif;
}
*{box-sizing:border-box;margin:0;padding:0}
html,body{width:1200px;height:2321px;overflow:hidden;background:var(--backdrop)}
.stage{position:absolute;left:81px;top:81px;width:1152px;height:2396px;transform:scale(0.9009);transform-origin:0 0;background:var(--page);font-family:var(--sans);color:var(--ink);overflow:hidden;box-shadow:0 6px 24px rgba(0,0,0,.25)}
.abs{position:absolute}

/* hero */
.hero-photo{left:0;top:0;width:1152px;height:600px;clip-path:polygon(0 0,100% 0,100% 465px,50% 600px,0 465px);
  background:linear-gradient(90deg,rgba(0,84,170,.97) 0%,rgba(0,84,170,.85) 30%,rgba(6,119,186,.35) 55%,rgba(202,222,239,.2) 100%),linear-gradient(180deg,#c9d3dc,#8e9aa6 70%,#6c7782)}
.brand{display:flex;align-items:center;gap:12px}
.brand-dot{width:52px;height:52px;border-radius:50%;background:var(--white);flex:none}
.brand-name{font-family:var(--serif);font-weight:600;font-size:22px;color:var(--white);line-height:1.1}
.brand-tag{font-size:10px;letter-spacing:1.5px;color:var(--white);margin-top:3px}
.nav{right:158px;top:18px;display:flex;gap:30px;font-size:11px;color:var(--ink)}
.btn-nav{left:1006px;top:12px;width:134px;height:26px;border-radius:8px;background:var(--blue-deep);color:var(--white);font-size:11px;font-weight:600;display:flex;align-items:center;justify-content:center}
.hero-title{left:64px;top:150px;font-family:var(--serif);font-weight:700;font-size:48px;line-height:50px;color:var(--white)}
.hero-sub{left:64px;top:265px;width:400px;font-size:17px;line-height:20px;color:var(--white)}
.btn-ghost{height:32px;border:1.5px solid var(--white);border-radius:16px;color:var(--white);font-size:12px;font-weight:600;display:flex;align-items:center;justify-content:center}
.seal{width:46px;height:46px;border-radius:50%;background:var(--white);border:4px solid var(--blue-deep)}

/* headings */
.serif-head{font-family:var(--serif);font-weight:700;color:var(--blue-deep);white-space:nowrap}
.dot{width:36px;height:36px;border-radius:50%;border:3px solid var(--blue-deep);background:var(--white)}
.pain-list{left:64px;top:708px;width:476px;list-style:none}
.pain-list li{display:flex;align-items:center;gap:8px;height:36.5px;font-size:12.5px;border-bottom:1px solid #dde3ec}
.photo-tablet{left:610px;top:660px;width:478px;height:233px;border-radius:14px;background:linear-gradient(120deg,#b8c2cc,#8a98a8 45%,#3f6aa3 100%)}

/* cards */
.card{background:var(--white);border-radius:8px;padding:20px 22px}
.card-line{border:1.5px solid var(--blue-pale);background:transparent}
.card-head{display:flex;align-items:center;gap:8px;margin-bottom:10px}
.icon{width:36px;height:36px;border-radius:50%;border:1.5px solid var(--blue-deep);flex:none}
.card-title{font-size:18px;font-weight:600;color:var(--blue-deep);white-space:nowrap}
.card-title.caps{font-size:15px;font-weight:700;line-height:17px;text-transform:uppercase}
.card-text{font-size:10.5px;line-height:14px;color:var(--ink)}
.band{left:0;top:1155px;width:1152px;height:290px;background:var(--band)}

/* quote */
.quote{left:64px;top:1745px;width:1024px;height:150px;text-align:center;padding-top:22px}
.quote p{font-family:var(--serif);font-weight:700;font-size:27px;line-height:36px;color:var(--blue-deep)}
.quote span{display:block;margin-top:22px;font-size:13px}

/* cta */
.cta{left:0;top:1955px;width:1152px;height:350px;background:var(--blue-deep);clip-path:polygon(50% 0,100% 110px,100% 100%,0 100%,0 110px)}
.cta-text{left:0;width:1152px;text-align:center;color:var(--white)}
.btn-solid{left:469px;top:2226px;width:214px;height:36px;border-radius:18px;background:var(--white);color:var(--blue-deep);font-size:15px;font-weight:600;display:flex;align-items:center;justify-content:center}
.footer{left:0;top:2305px;width:1152px;height:91px;background:#024f9f;color:var(--white)}
</style>
</head>
<body>
<div class="stage">

  <div class="abs hero-photo" role="img" aria-label="Food production floor with staff in hairnets and masks inspecting a conveyor line"></div>

  <div class="abs brand" style="left:18px;top:5px">
    <div class="brand-dot"></div>
    <div><div class="brand-name">Northline Consulting Group</div><div class="brand-tag">FOOD SAFETY &amp; QFS CERTIFICATION</div></div>
  </div>
  <nav class="abs nav"><span>Home</span><span>About us</span><span>Services</span><span>Team</span><span>Contact</span></nav>
  <div class="abs btn-nav">Get QFS Consultation</div>

  <h1 class="abs hero-title">Pass your QFS audit<br>with confidence.</h1>
  <p class="abs hero-sub">We help food manufacturers build practical<br>systems that work on the production floor<br>-not just on audit day</p>
  <div class="abs btn-ghost" style="left:64px;top:353px;width:160px">Explore Services</div>
  <div class="abs btn-ghost" style="left:235px;top:353px;width:160px">Get QFS Consultation</div>

  <div class="abs seal" style="left:553px;top:577px"></div>

  <!-- struggle -->
  <div class="abs dot" style="left:68px;top:656px"></div>
  <h2 class="abs serif-head" style="left:118px;top:652px;font-size:31px">Struggling with QFScertification?</h2>
  <ul class="abs pain-list">
    <li><svg width="12" height="12" viewBox="0 0 12 12"><path d="M1 6l3.5 4L11 1" fill="none" stroke="#0054AA" stroke-width="2.5"/></svg>An audit failure or close call</li>
    <li><svg width="12" height="12" viewBox="0 0 12 12"><path d="M1 6l3.5 4L11 1" fill="none" stroke="#0054AA" stroke-width="2.5"/></svg>Disorganized or out-of-date records</li>
    <li><svg width="12" height="12" viewBox="0 0 12 12"><path d="M1 6l3.5 4L11 1" fill="none" stroke="#0054AA" stroke-width="2.5"/></svg>QC systems that don't work in real production</li>
    <li><svg width="12" height="12" viewBox="0 0 12 12"><path d="M1 6l3.5 4L11 1" fill="none" stroke="#0054AA" stroke-width="2.5"/></svg>An overwhelmed, undertrained team</li>
  </ul>
  <div class="abs photo-tablet" role="img" aria-label="Hands holding a tablet showing a food safety compliance checklist in a plant"></div>

  <h2 class="abs serif-head" style="left:64px;top:872px;font-size:31px;line-height:36px">Pass your QFS audit with less stress,<br>less paperwork, and year-round support.</h2>

  <div class="abs card" style="left:64px;top:973px;width:238px;height:125px"><div class="card-head"><div class="icon"></div><div class="card-title">Program Design</div></div><p class="card-text">HACCP plans, SOPs, forms, logs, and supporting documentation tailored to your facility.</p></div>
  <div class="abs card" style="left:326px;top:973px;width:238px;height:125px"><div class="card-head"><div class="icon"></div><div class="card-title">Digital Build</div></div><p class="card-text">Move your program into modern software like PlantLog or SafeTrack.</p></div>
  <div class="abs card" style="left:588px;top:973px;width:238px;height:125px;padding-top:26px"><div class="card-head"><div class="icon"></div><div class="card-title">Coaching</div></div><p class="card-text">Train your team to own the system day-to-day and stay audit-ready.</p></div>
  <div class="abs card" style="left:850px;top:973px;width:238px;height:125px;padding:26px 12px 20px 18px"><div class="card-head"><div class="icon"></div><div class="card-title">Bilingual Support</div></div><p class="card-text">Support for Spanish-speaking floor teams and documentation needs.</p></div>

  <!-- how we help -->
  <div class="abs band"></div>
  <div class="abs dot" style="left:444px;top:1218px;width:40px;height:40px"></div>
  <h2 class="abs serif-head" style="left:497px;top:1215px;font-size:31px">HOW WE HELP</h2>
  <div class="abs card card-line" style="left:64px;top:1280px;width:238px;height:112px"><div class="card-head"><div class="icon"></div><div class="card-title caps">Pass your<br>audit</div></div><p class="card-text">We build guarnted audit-ready systems, tailored to your plant.</p></div>
  <div class="abs card card-line" style="left:326px;top:1280px;width:238px;height:112px;padding:20px 8px 20px 16px"><div class="card-head"><div class="icon"></div><div class="card-title caps">Eliminate<br>paperwork chaos</div></div><p class="card-text">We digitilize your QFS the non into easy-to-use continate.</p></div>
  <div class="abs card card-line" style="left:588px;top:1280px;width:238px;height:112px"><div class="card-head"><div class="icon"></div><div class="card-title caps">Train your<br>team to own it</div></div><p class="card-text">Train your team to own the system day-to-day and stay audit-ready.</p></div>
  <div class="abs card card-line" style="left:850px;top:1280px;width:238px;height:112px"><div class="card-head"><div class="icon"></div><div class="card-title caps">Stay audit-<br>ready</div></div><p class="card-text">Support for Spanish-speaking floor teams and documentation needs.</p></div>

  <!-- certified path -->
  <div class="abs dot" style="left:374px;top:1486px;width:40px;height:40px"></div>
  <h2 class="abs serif-head" style="left:428px;top:1483px;font-size:31px">How We Get You Certified</h2>
  <p class="abs" style="left:0;top:1538px;width:1152px;text-align:center;font-size:12.5px">A clear path that removes guesswork and helps your facility move toward QFS with structure.</p>
  <div class="abs card" style="left:64px;top:1575px;width:238px;height:125px"><div class="card-head"><div class="icon"></div><div class="card-title caps">01- Assess your<br>current gaps</div></div><p class="card-text">We learn about your facility, current systems, and where you are in the QFS journey.</p></div>
  <div class="abs card" style="left:326px;top:1575px;width:238px;height:125px"><div class="card-head"><div class="icon"></div><div class="card-title caps">02- Build your<br>QFS system</div></div><p class="card-text">We identify missing pieces, review priorities, and create a practical roadmap.</p></div>
  <div class="abs card" style="left:588px;top:1575px;width:238px;height:125px"><div class="card-head"><div class="icon"></div><div class="card-title caps">03- Implement it<br>with your team</div></div><p class="card-text">We create the program, forms, logs, and workflow directly inside your digital platform.</p></div>
  <div class="abs card" style="left:850px;top:1575px;width:238px;height:125px"><div class="card-head"><div class="icon"></div><div class="card-title caps">04- Prepare for<br>certification</div></div><p class="card-text">We train your team, run mock audits, and support you through certification day.</p></div>

  <div class="abs card quote"><p>“Northline Consulting Group did not just hand us a binder. They built our<br>entire QFS system into software and coached our team until we owned it.”</p><span>— QFS-Certified Manufacturing Client</span></div>

  <!-- cta -->
  <div class="abs cta"></div>
  <div class="abs seal" style="left:553px;top:1937px"></div>
  <p class="abs cta-text" style="top:2028px;font-size:15px">READY TO TAKE THE NEXT STEP?</p>
  <h2 class="abs cta-text" style="top:2060px;font-family:var(--serif);font-weight:700;font-size:41px;line-height:43px">NEED A PARTNER WHO<br>UNDERSTANDS MANUFACTURING REALITIES?</h2>
  <p class="abs cta-text" style="top:2155px;font-size:16.5px;line-height:22px">Use this concept as the core website homepage and connect it with the Services<br>and Contact pages included in this package.</p>
  <div class="abs btn-solid">OPEN CONTACT PAGE</div>

  <footer class="abs footer">
    <div class="abs brand" style="left:38px;top:22px;gap:10px">
      <div class="brand-dot" style="width:36px;height:36px"></div>
      <div><div class="brand-name" style="font-size:17px">Northline Consulting Group</div><div class="brand-tag" style="font-size:8px">FOOD SAFETY &amp; QFS CERTIFICATION</div></div>
    </div>
    <p class="abs" style="left:426px;top:30px;width:300px;text-align:center;font-size:10px;line-height:15px">Tech-driven QFS consulting for food<br>and beverage manufacturers.</p>
    <p class="abs" style="left:850px;top:30px;width:240px;text-align:center;font-size:10px;line-height:15px"><b>CALL TO ACTION</b><br>Get QFS Consultation &nbsp;|&nbsp; View Service Details</p>
  </footer>
</div>
</body>
</html>
```